依頼詳細
シーズー専門ペットショップ「モフリン」のお客様配布用の2016年 A2版カレンダー作成
記載項目
・作成サイズは 規格A2(420×594ミリ)

・CMYK4色 特色利用不可

・提供された画像をメインにデザインをお願い致します。

・デザインに特に制限はございませんが、明るくかわいらしい感じを希望します。

・「CALENDAR 2016」の様な表記は不要です。

・店舗ロゴ(ワンちゃんの美容室 モフリン・ロゴデータ有)、犬舎名(シーズー専門犬舎 SILVER MEADOW HANAE JP・データ有)、・住所(石川県小松市桜見町丙12-8)・電話(PHONE/FAX 0761-48-5926)、は必ずどこかに入れてください。

・2016年1月から12月までで作成お願いします。なお、カレンダーの玉は、作成者様のお持ちの他データからの流用でも構いませんが、作成者様が校正をお願いします。

・カレンダーの六曜は不要です。
希望イメージ
シンプル 複雑
単色 カラフル
暗い 明るい
日常 高級
遊び心 厳粛
未来的 伝統的
女性的 男性的
希望する色
設定なし
納品ファイル
• 高解像度JPG (.jpg)
• イラストレーター形式 (.ai)
補足説明
最終的な納品時にイラストレータCS2(アウトラインと未アウトライン)形式にて納品いただきます。
また、ご希望される場合、印刷後のカレンダーを数部贈呈いたします。
過去の決定案の画像をアップします。
期間延長いたします。
■ 選んだ理由

可愛らしいデザインが気に入りました。

■ 提案者全員のお礼・コメント

有り難うございます。よかったら来年もご参加お願いします。

```html
<!DOCTYPE html>
<html lang="ja">
<head>
<meta charset="utf-8">
<title>モフリン 2016 カレンダー</title>
<link rel="stylesheet" href="https://fonts.googleapis.com/css2?family=M+PLUS+Rounded+1c:wght@500;800&display=swap">
<style>
:root{
  --pink:#f4a6b4;
  --pink-deep:#e9869a;
  --fur-light:#f3ece2;
  --fur-mid:#c9a77a;
  --fur-dark:#6e4a2c;
  --sky:#dff1fb;
  --red:#e0262b;
  --ink:#333;
  --name:#e94f8a;
  --blue:#8fc8ee;
  --rose:#f5b3c8;
  --orange:#f9c48d;
  --green:#b5df9c;
  --violet:#c6b6e8;
  --yellow:#f6e48a;
  --white:#fff;
}
*{margin:0;padding:0;box-sizing:border-box}
html,body{width:848px;height:1200px;overflow:hidden;background:var(--white)}
body{font-family:"M PLUS Rounded 1c",sans-serif;color:var(--ink)}
.calendar-sheet{position:relative;width:848px;height:1200px;background:var(--white)}

.hero{position:absolute;left:0;top:0;width:848px;height:672px;
  background:
    radial-gradient(ellipse 190px 330px at 220px 300px,var(--fur-light) 0%,var(--fur-mid) 55%,rgba(201,167,122,0) 100%),
    radial-gradient(ellipse 200px 340px at 640px 300px,var(--fur-light) 0%,var(--fur-mid) 55%,rgba(201,167,122,0) 100%),
    linear-gradient(180deg,var(--pink) 0%,var(--pink) 62%,var(--sky) 78%,#9fcf8a 100%);}
.hero-name{position:absolute;left:50%;top:240px;transform:translateX(-50%);
  font-weight:800;font-size:74px;letter-spacing:4px;color:var(--name);white-space:nowrap}

.months{position:absolute;left:28px;top:690px;width:792px;height:418px;
  display:grid;grid-template-columns:repeat(3,1fr);grid-template-rows:repeat(4,1fr);column-gap:30px}
.month{position:relative;padding-top:2px}
.month-num{font-weight:800;font-size:24px;line-height:24px;margin-left:4px}
.days{position:relative;display:grid;grid-template-columns:repeat(7,1fr);grid-auto-rows:13px;
  font-size:11px;line-height:13px;font-weight:500;text-align:center;margin-top:1px}
.days i{font-style:normal;position:relative;z-index:1}
.days i.sun{color:var(--red)}
.tint{position:absolute;top:-20px;width:30px;height:92px;border-radius:15px;opacity:.55;z-index:0}
.m-blue .month-num{color:#3a8fd0}.m-blue .tint{background:var(--blue)}
.m-rose .month-num{color:#e0558a}.m-rose .tint{background:var(--rose)}
.m-orange .month-num{color:#ec8a2a}.m-orange .tint{background:var(--orange)}
.m-green .month-num{color:#55a83a}.m-green .tint{background:var(--green)}
.m-violet .month-num{color:#8060c4}.m-violet .tint{background:var(--violet)}
.m-yellow .month-num{color:#d2ad12}.m-yellow .tint{background:var(--yellow)}

.footer{position:absolute;left:0;top:1112px;width:848px;height:88px;border-top:3px solid var(--pink-deep);
  display:flex;align-items:center;justify-content:space-between;padding:0 24px}
.salon{width:260px}
.salon-label{display:inline-block;background:var(--red);color:var(--white);font-weight:800;font-size:17px;
  padding:3px 10px;border-radius:4px}
.kennel-type{font-size:12px;font-weight:800;margin-top:4px;color:var(--red)}
.kennel-name{font-size:13px;font-weight:800;color:var(--red);letter-spacing:.5px}
.shop-name{font-weight:800;font-size:38px;color:var(--name);letter-spacing:3px}
.contact{width:250px;text-align:right;font-size:13px;font-weight:800;line-height:20px;color:var(--red)}
</style>
</head>
<body>
<div class="calendar-sheet">

  <div class="hero" role="img" aria-label="ピンクの肉球柄の背景に並ぶ2匹のシーズー、赤い飛行機に乗ったキャラクターと街並みのイラスト"></div>
  <div class="hero-name">モフリン</div>

  <div class="months">
    <section class="month m-blue"><div class="month-num">1</div><div class="days"><span class="tint" style="left:100px"></span>
      <i style="grid-column-start:6">1</i><i>2</i><i class="sun">3</i><i>4</i><i>5</i><i>6</i><i>7</i><i>8</i><i>9</i><i class="sun">10</i><i>11</i><i>12</i><i>13</i><i>14</i><i>15</i><i>16</i><i class="sun">17</i><i>18</i><i>19</i><i>20</i><i>21</i><i>22</i><i>23</i><i class="sun">24</i><i>25</i><i>26</i><i>27</i><i>28</i><i>29</i><i>30</i><i class="sun">31</i></div></section>
    <section class="month m-rose"><div class="month-num">2</div><div class="days"><span class="tint" style="left:140px"></span>
      <i style="grid-column-start:2">1</i><i>2</i><i>3</i><i>4</i><i>5</i><i>6</i><i class="sun">7</i><i>8</i><i>9</i><i>10</i><i>11</i><i>12</i><i>13</i><i class="sun">14</i><i>15</i><i>16</i><i>17</i><i>18</i><i>19</i><i>20</i><i class="sun">21</i><i>22</i><i>23</i><i>24</i><i>25</i><i>26</i><i>27</i><i class="sun">28</i><i>29</i></div></section>
    <section class="month m-orange"><div class="month-num">3</div><div class="days"><span class="tint" style="left:70px"></span>
      <i style="grid-column-start:3">1</i><i>2</i><i>3</i><i>4</i><i>5</i><i class="sun">6</i><i>7</i><i>8</i><i>9</i><i>10</i><i>11</i><i>12</i><i class="sun">13</i><i>14</i><i>15</i><i>16</i><i>17</i><i>18</i><i>19</i><i class="sun">20</i><i>21</i><i>22</i><i>23</i><i>24</i><i>25</i><i>26</i><i class="sun">27</i><i>28</i><i>29</i><i>30</i><i>31</i></div></section>

    <section class="month m-green"><div class="month-num">4</div><div class="days"><span class="tint" style="left:110px"></span>
      <i style="grid-column-start:6">1</i><i>2</i><i class="sun">3</i><i>4</i><i>5</i><i>6</i><i>7</i><i>8</i><i>9</i><i class="sun">10</i><i>11</i><i>12</i><i>13</i><i>14</i><i>15</i><i>16</i><i class="sun">17</i><i>18</i><i>19</i><i>20</i><i>21</i><i>22</i><i>23</i><i class="sun">24</i><i>25</i><i>26</i><i>27</i><i>28</i><i>29</i><i>30</i></div></section>
    <section class="month m-violet"><div class="month-num">5</div><div class="days"><span class="tint" style="left:75px"></span>
      <i class="sun">1</i><i>2</i><i>3</i><i>4</i><i>5</i><i>6</i><i>7</i><i class="sun">8</i><i>9</i><i>10</i><i>11</i><i>12</i><i>13</i><i>14</i><i class="sun">15</i><i>16</i><i>17</i><i>18</i><i>19</i><i>20</i><i>21</i><i class="sun">22</i><i>23</i><i>24</i><i>25</i><i>26</i><i>27</i><i>28</i><i class="sun">29</i><i>30</i><i>31</i></div></section>
    <section class="month m-yellow"><div class="month-num">6</div><div class="days"><span class="tint" style="left:145px"></span>
      <i style="grid-column-start:4">1</i><i>2</i><i>3</i><i>4</i><i class="sun">5</i><i>6</i><i>7</i><i>8</i><i>9</i><i>10</i><i>11</i><i class="sun">12</i><i>13</i><i>14</i><i>15</i><i>16</i><i>17</i><i>18</i><i class="sun">19</i><i>20</i><i>21</i><i>22</i><i>23</i><i>24</i><i>25</i><i class="sun">26</i><i>27</i><i>28</i><i>29</i><i>30</i></div></section>

    <section class="month m-rose"><div class="month-num">7</div><div class="days"><span class="tint" style="left:105px"></span>
      <i style="grid-column-start:6">1</i><i>2</i><i class="sun">3</i><i>4</i><i>5</i><i>6</i><i>7</i><i>8</i><i>9</i><i class="sun">10</i><i>11</i><i>12</i><i>13</i><i>14</i><i>15</i><i>16</i><i class="sun">17</i><i>18</i><i>19</i><i>20</i><i>21</i><i>22</i><i>23</i><i class="sun">24</i><i>25</i><i>26</i><i>27</i><i>28</i><i>29</i><i>30</i><i class="sun">31</i></div></section>
    <section class="month m-blue"><div class="month-num">8</div><div class="days"><span class="tint" style="left:70px"></span>
      <i style="grid-column-start:2">1</i><i>2</i><i>3</i><i>4</i><i>5</i><i>6</i><i class="sun">7</i><i>8</i><i>9</i><i>10</i><i>11</i><i>12</i><i>13</i><i class="sun">14</i><i>15</i><i>16</i><i>17</i><i>18</i><i>19</i><i>20</i><i class="sun">21</i><i>22</i><i>23</i><i>24</i><i>25</i><i>26</i><i>27</i><i class="sun">28</i><i>29</i><i>30</i><i>31</i></div></section>
    <section class="month m-green"><div class="month-num">9</div><div class="days"><span class="tint" style="left:140px"></span>
      <i style="grid-column-start:5">1</i><i>2</i><i>3</i><i class="sun">4</i><i>5</i><i>6</i><i>7</i><i>8</i><i>9</i><i>10</i><i class="sun">11</i><i>12</i><i>13</i><i>14</i><i>15</i><i>16</i><i>17</i><i class="sun">18</i><i>19</i><i>20</i><i>21</i><i>22</i><i>23</i><i>24</i><i class="sun">25</i><i>26</i><i>27</i><i>28</i><i>29</i><i>30</i></div></section>

    <section class="month m-orange"><div class="month-num">10</div><div class="days"><span class="tint" style="left:110px"></span>
      <i style="grid-column-start:7">1</i><i class="sun">2</i><i>3</i><i>4</i><i>5</i><i>6</i><i>7</i><i>8</i><i class="sun">9</i><i>10</i><i>11</i><i>12</i><i>13</i><i>14</i><i>15</i><i class="sun">16</i><i>17</i><i>18</i><i>19</i><i>20</i><i>21</i><i>22</i><i class="sun">23</i><i>24</i><i>25</i><i>26</i><i>27</i><i>28</i><i>29</i><i class="sun">30</i><i>31</i></div></section>
    <section class="month m-yellow"><div class="month-num">11</div><div class="days"><span class="tint" style="left:75px"></span>
      <i style="grid-column-start:3">1</i><i>2</i><i>3</i><i>4</i><i>5</i><i class="sun">6</i><i>7</i><i>8</i><i>9</i><i>10</i><i>11</i><i>12</i><i class="sun">13</i><i>14</i><i>15</i><i>16</i><i>17</i><i>18</i><i>19</i><i class="sun">20</i><i>21</i><i>22</i><i>23</i><i>24</i><i>25</i><i>26</i><i class="sun">27</i><i>28</i><i>29</i><i>30</i></div></section>
    <section class="month m-violet"><div class="month-num">12</div><div class="days"><span class="tint" style="left:140px"></span>
      <i style="grid-column-start:5">1</i><i>2</i><i>3</i><i class="sun">4</i><i>5</i><i>6</i><i>7</i><i>8</i><i>9</i><i>10</i><i class="sun">11</i><i>12</i><i>13</i><i>14</i><i>15</i><i>16</i><i>17</i><i class="sun">18</i><i>19</i><i>20</i><i>21</i><i>22</i><i>23</i><i>24</i><i class="sun">25</i><i>26</i><i>27</i><i>28</i><i>29</i><i>30</i><i>31</i></div></section>
  </div>

  <footer class="footer">
    <div class="salon">
      <div class="salon-label">ワンちゃんの美容室</div>
      <div class="kennel-type">シーズー専門犬舎</div>
      <div class="kennel-name">SILVER MEADOW HANAE JP</div>
    </div>
    <div class="shop-name">モフリン</div>
    <div class="contact">
      <div>石川県小松市桜見町丙12-8</div>
      <div>PHONE/FAX 0761-48-5926</div>
    </div>
  </footer>

</div>
</body>
</html>
```